looking for sleek business card to standout from the crowd!

We are a young biotechnology company looking to help you personalize your health through understanding your genetic make up. We need you help in making a clean but sleek business card design using our new logo. The goal? Any time we give our cards out, people say "nice card!" The feel we are going for is "modern-techy". We don't want to come across as an old, giant pharma company, but not trying to be a hipster either.

Target Market(s)

healthcare and biotechnology industry.

Industry/Entity Type

Biotechnology

Contact Information for Business Card

Info to include on the card will be NAME, TITLE, EMAIL, PHONE. The companies website (www.corvalinbio.com) should also be on the card some where. Would like the logo, when printed, to be raised.

Requirements
Must have
• The logo we have attached in the color it is in. Fonts for text should lean toward more professional/tech.
Nice to have
• Prefer white/light color background
Should not have
• cartoons, landscape backgrounds images.

```html
<!DOCTYPE html>
<html lang="en">
<head>
<meta charset="utf-8">
<title>Corvalin Business Card</title>
<link rel="stylesheet" href="https://fonts.googleapis.com/css2?family=Open+Sans:wght@400;600;700&display=swap">
<style>
  :root {
    --stage: #3a332f;
    --card: #131416;
    --card-edge: #1d1e21;
    --blue: #2f7fd0;
    --green: #7fcf3a;
    --ink: #f2f2f2;
    --muted: #8c8f94;
    --rule: #55585d;
    --emboss: #3b3d41;
  }
  * { box-sizing: border-box; margin: 0; padding: 0; }
  html, body {
    width: 1200px; height: 864px; overflow: hidden;
    background: var(--stage);
    font-family: "Open Sans", Arial, sans-serif;
  }
  .canvas { position: relative; width: 1200px; height: 864px; }
  .card {
    position: absolute;
    width: 525px; height: 300px;
    background: var(--card);
    border: 1px solid var(--card-edge);
    border-radius: 4px;
    box-shadow: 0 18px 40px rgba(0,0,0,.45);
  }
  .card-back { left: 50px; top: 110px; }
  .card-front { left: 625px; top: 454px; }

  /* back */
  .back-mark {
    position: absolute; left: 0; right: 0; top: 92px;
    display: flex; align-items: center; justify-content: center; gap: 14px;
  }
  .back-mark .dot {
    width: 26px; height: 26px; border-radius: 50%;
    background: var(--emboss);
  }
  .back-mark .wordmark {
    font-weight: 700; font-size: 46px; letter-spacing: 2px;
    color: var(--emboss);
  }
  .back-url {
    position: absolute; left: 0; right: 0; top: 200px;
    text-align: center; font-size: 13px; letter-spacing: 1px;
    color: var(--muted);
  }

  /* front */
  .front-mark {
    position: absolute; left: 52px; top: 62px;
    display: flex; align-items: center; gap: 14px;
  }
  .front-mark .wordmark {
    font-weight: 700; font-size: 48px; letter-spacing: 1px;
    color: var(--blue); line-height: 1;
  }
  .front-mark .dot {
    width: 60px; height: 60px; border-radius: 50%;
    background: var(--green);
  }
  .identity {
    position: absolute; left: 40px; top: 186px; width: 170px;
    text-align: right;
  }
  .identity .name { font-size: 17px; font-weight: 600; color: var(--blue); }
  .identity .title { font-size: 15px; color: var(--green); margin-top: 2px; }
  .divider {
    position: absolute; left: 226px; top: 178px;
    width: 1px; height: 74px; background: var(--rule);
  }
  .contact-list {
    position: absolute; left: 244px; top: 178px;
    list-style: none;
  }
  .contact-list li {
    display: flex; align-items: center; gap: 10px;
    font-size: 14px; color: var(--ink); height: 25px;
  }
  .contact-list svg { width: 14px; height: 14px; fill: var(--blue); flex: none; }
</style>
</head>
<body>
<main class="canvas">
  <section class="card card-back" aria-label="Card back">
    <div class="back-mark">
      <span class="dot"></span>
      <span class="wordmark">CORVALIN</span>
    </div>
    <p class="back-url">www.corvalinbio.com</p>
  </section>

  <section class="card card-front" aria-label="Card front">
    <div class="front-mark">
      <span class="wordmark">CORVALIN</span>
      <span class="dot"></span>
    </div>
    <div class="identity">
      <p class="name">Mara Lindqvist</p>
      <p class="title">President</p>
    </div>
    <div class="divider"></div>
    <ul class="contact-list">
      <li>
        <svg viewBox="0 0 24 24" aria-hidden="true"><path d="M6.6 10.8a15.1 15.1 0 0 0 6.6 6.6l2.2-2.2a1 1 0 0 1 1-.25 11.4 11.4 0 0 0 3.6.57 1 1 0 0 1 1 1V20a1 1 0 0 1-1 1A17 17 0 0 1 3 4a1 1 0 0 1 1-1h3.5a1 1 0 0 1 1 1c0 1.25.2 2.45.57 3.6a1 1 0 0 1-.25 1z"/></svg>
        555 0142 7781
      </li>
      <li>
        <svg viewBox="0 0 24 24" aria-hidden="true"><path d="M2 5h20v14H2zm2 2v.5l8 5 8-5V7l-8 5z"/></svg>
        mlind@corvalinbio.com
      </li>
      <li>
        <svg viewBox="0 0 24 24" aria-hidden="true"><path d="M12 2a10 10 0 1 0 0 20 10 10 0 0 0 0-20zm0 2c1 1.3 1.8 3.3 2.1 5H9.9C10.2 7.3 11 5.3 12 4zM4.3 11h3.6c0 .7 0 1.3.1 2H4.3a8 8 0 0 1 0-2zm5.6 0h4.2a14 14 0 0 1 0 2H9.9a14 14 0 0 1 0-2zm6.2 0h3.6a8 8 0 0 1 0 2H16c.1-.7.1-1.3.1-2zM12 20c-1-1.3-1.8-3.3-2.1-5h4.2c-.3 1.7-1.1 3.7-2.1 5z"/></svg>
        www.corvalinbio.com
      </li>
    </ul>
  </section>
</main>
</body>
</html>
```